Report-Design  für Social-Media-Beratungs-Agentur
Report-Design für Social-Media-Beratungs-Agentur
Zielgruppe
Wir sind eine Social-Media-Beratungs-Agentur, die KMU bei der strategischen Ausrichtung und Umsetzung ihrer Social-Media-Präsenzen berät und unterstützt.
Aufgabenstellung
Wir analysieren die KarriNetz Profile von Unternehmen in einer Excel-Datei, indem wir in einem Reiter verschiedene Aspekte bewerten. Aus diesen Bewertungen ergibt sich dann in einem zweiten Reiter ein Report (hängt hier an), in den die Ergebnisse aus der 1. Mappe automatisch übernommen werden. Dieser Report wird als PDF gespeichert und an den Kunden geschickt. Wir möchten das Report-Design gerne neu gestalten lassen: Es soll zeitgemäß, professionell und kompetent wirken und nicht mehr 'wie in Excel zusammengebastelt'. Ein Beispiel für ein Design, das uns gefällt, hängt als Inspiration an. Gerne können Grafikelemente aus Canva oder anderen Grafikprogrammen eingefügt werden. Wichtig ist, dass die Struktur mit den Zellen, in die Daten automatisch übernommen werden (im Anhang durch # gekennzeichnet), erhalten bleibt. Unsere Firmenfarben sind: #f69f25, #11323a, #809398, #fcfefd. Wir haben noch weitere Analysen, die wir bei Erfolg dieses Auftrags ebenfalls gerne optimieren lassen möchten.

```html
<!DOCTYPE html>
<html lang="de">
<head>
<meta charset="utf-8">
<title>Feedwerk – Social Media Performance Report Q3 2024</title>
<link rel="stylesheet" href="https://fonts.googleapis.com/css2?family=Inter:wght@400;500;600&display=swap">
<style>
:root{
  --brand-orange:#f69f25;
  --brand-teal:#11323a;
  --brand-slate:#809398;
  --brand-paper:#fcfefd;
  --orange-soft:#fbd39b;
  --slate-soft:#d3dcdd;
  --slate-tint:#e3e9ea;
  --stage:#a9b3b6;
  --ink:#11323a;
  --muted:#4d5f64;
  --line:#e2e7e8;
}
*{box-sizing:border-box;margin:0;padding:0}
html,body{width:1200px;height:900px;overflow:hidden}
body{background:var(--stage);font-family:"Inter",Arial,sans-serif;color:var(--ink);position:relative}
.panel{position:absolute;background:var(--brand-paper);border-radius:14px;overflow:hidden}
.abs{position:absolute}
.panel-head{position:absolute;top:13px;display:flex;align-items:center;gap:6px;font-size:10px;font-weight:500;white-space:nowrap}
.panel-head::before{content:"";width:10px;height:10px;border-radius:50%;background:var(--brand-teal)}
.body-text{font-size:7.4px;line-height:10.4px;color:var(--muted)}
.lead-text{font-size:8px;line-height:10.6px;color:var(--ink);font-weight:500}
.photo{position:absolute;border-radius:8px}
/* cover */
.cover{left:25px;top:40px;width:374px;height:821px}
.brand{left:25px;top:21px;display:flex;align-items:center;gap:7px;font-size:15px;font-weight:600}
.brand-dot{width:18px;height:18px;border-radius:50%;background:var(--brand-orange)}
.pill{position:absolute;top:19px;height:22px;border-radius:11px;font-size:8px;color:var(--brand-paper);display:flex;align-items:center;justify-content:center}
.pill-orange{left:234px;width:60px;background:var(--brand-orange);color:var(--brand-teal)}
.pill-teal{left:300px;width:56px;background:var(--brand-teal)}
.cover-title{left:27px;top:86px;font-size:38px;line-height:40.5px;font-weight:500;letter-spacing:-0.8px}
.hero{left:17px;top:270px;width:340px;height:363px;border-radius:12px;background:linear-gradient(135deg,#c9b9a6 0%,#8d6e55 45%,#3f3a3b 100%)}
.hero-chip{position:absolute;left:14px;top:12px;background:var(--brand-paper);border-radius:12px;padding:6px 12px;font-size:8px;font-weight:500;display:flex;gap:6px;align-items:center}
.hero-chip::before{content:"";width:7px;height:7px;border-radius:50%;background:var(--brand-teal)}
.tile{position:absolute;border-radius:8px;font-size:7px;line-height:9px;padding:9px 8px}
.tile-orange{left:17px;top:650px;width:78px;height:47px;background:var(--brand-orange);color:var(--brand-teal)}
.tile-slate{left:101px;top:650px;width:74px;height:47px;background:var(--brand-slate);color:var(--brand-paper)}
.tile-wave{left:181px;top:650px;width:176px;height:150px;background:var(--slate-tint);border:1px solid var(--line)}
.tile-photo-a{left:17px;top:703px;width:78px;height:97px;background:linear-gradient(160deg,#e7e4e0,#c89a83)}
.tile-photo-b{left:101px;top:703px;width:74px;height:97px;background:linear-gradient(160deg,#c9c7c4,#d99a45)}
/* strategy */
.strategy{left:414px;top:40px;width:374px;height:265px}
.tag-line{left:16px;top:44px;font-size:7.5px;color:var(--muted)}
.tag-line em{font-style:normal;color:var(--brand-orange)}
.tag-line b{font-weight:400;color:var(--brand-slate)}
.thumbs{left:16px;top:67px;display:flex;gap:4px}
.thumbs span{width:55px;height:46px;border-radius:5px}
/* chart panel */
.trend{left:802px;top:40px;width:373px;height:265px}
/* bars */
.bars{left:414px;top:319px;width:374px;height:262px}
.chart-title{left:31px;top:35px;font-size:11.5px;font-weight:500}
/* cards */
.cards{left:802px;top:319px;width:373px;height:262px}
.card{position:absolute;top:39px;width:160px;height:185px;border-radius:10px;padding:18px 15px}
.card-orange{left:18px;background:var(--brand-orange);color:var(--brand-teal)}
.card-slate{left:196px;background:var(--slate-soft);color:var(--brand-teal)}
.card h3{font-size:11px;line-height:14px;font-weight:500;margin-bottom:10px}
.card p{font-size:6.6px;line-height:9px;margin-bottom:7px}
.chips{position:absolute;top:237px;display:flex;gap:4px;align-items:center}
.chip{height:12px;border-radius:6px;background:var(--slate-tint);display:flex;align-items:center;gap:3px;padding:0 5px 0 2px;font-size:5.5px;color:var(--muted)}
.chip i{width:9px;height:9px;border-radius:50%;display:block}
/* feature panels */
.feature{width:374px;height:265px;top:596px}
.feature-a{left:414px}
.feature-b{left:802px;width:373px}
.feature-title{left:16px;top:50px;font-size:12px;line-height:15px;font-weight:500;width:170px}
.feature-sub{left:16px;top:92px;font-size:8px;color:var(--brand-orange);font-weight:500}
.action-bar{position:absolute;left:16px;top:222px;width:343px;height:21px;border-radius:11px;background:var(--brand-teal);color:var(--brand-paper);font-size:6.5px;display:flex;align-items:center;padding-left:10px;gap:6px}
.action-bar::before{content:"";width:8px;height:6px;border:1px solid var(--brand-paper);border-radius:1px}
</style>
</head>
<body>

<section class="panel cover">
  <div class="abs brand"><span class="brand-dot"></span>Feedwerk</div>
  <span class="pill pill-orange">Kontakt</span>
  <span class="pill pill-teal">Q3</span>
  <h1 class="abs cover-title">Social Media<br>Performance<br>Report -<br>Q3 2024</h1>
  <div class="abs hero" role="img" aria-label="Foto: Team schaut gemeinsam lachend auf Smartphone und Laptop">
    <span class="hero-chip">Social Feed Check</span>
  </div>
  <div class="tile tile-orange">Reichweite<br>Quartal</div>
  <div class="tile tile-slate">Profil Score<br>Übersicht</div>
  <div class="tile tile-wave" role="img" aria-label="Dekoratives Wellenmuster in Hellgrau"></div>
  <div class="tile tile-photo-a" role="img" aria-label="Foto: springende Person vor hellem Hintergrund"></div>
  <div class="tile tile-photo-b" role="img" aria-label="Foto: Arbeitstisch mit Geräten von oben"></div>
</section>

<section class="panel strategy">
  <div class="panel-head" style="left:16px">Social Media Strategy</div>
  <div class="panel-head" style="left:171px">Social Media 2024</div>
  <p class="abs tag-line">Fokus <em>Community Aufbau</em> <b>und Reichweite</b></p>
  <div class="abs thumbs" role="img" aria-label="Fotoreihe: Menschen beim Arbeiten mit Social Media">
    <span style="background:linear-gradient(160deg,#d8d2c8,#8f8475)"></span>
    <span style="background:linear-gradient(160deg,#bfb5a8,#5a4a3f)"></span>
    <span style="background:linear-gradient(160deg,#d6c9b9,#9a7a5f)"></span>
    <span style="background:linear-gradient(160deg,#e0b88f,#7a4f33)"></span>
    <span style="background:linear-gradient(160deg,#c7b8a5,#6e5a48)"></span>
    <span style="background:linear-gradient(160deg,#e3e1dd,#a89d91)"></span>
  </div>
  <p class="abs lead-text" style="left:16px;top:127px;width:330px">Unsere Analyse zeigt deutliches Wachstum auf allen Kanälen, vor allem bei Interaktionen und neuen Kontakten im Netzwerk.</p>
  <p class="abs body-text" style="left:16px;top:151px;width:330px">Im dritten Quartal haben wir Profil, Beiträge und Reaktionen detailliert bewertet. Die Inhalte erreichen mehr relevante Entscheider als zuvor, und die Interaktionsrate liegt klar über dem Branchenschnitt. Besonders Beiträge mit Bildern und kurzen Fragen erzielten hohe Reichweite. Beim Profil empfehlen wir ein aktualisiertes Titelbild, eine präzisere Beschreibung und regelmäßige Veröffentlichungen an festen Tagen. Die Zahl der Follower stieg stetig, neue Kontakte kamen vor allem aus der Zielgruppe. Für das nächste Quartal planen wir gezielte Formate und eine engere Abstimmung mit dem Vertrieb.</p>
</section>

<section class="panel trend">
  <div class="panel-head" style="left:16px">Social Strategy</div>
  <p class="abs body-text" style="left:16px;top:52px;width:335px">Die Kurve zeigt die Entwicklung der Reichweite und der Interaktionen je Woche im Quartal. Nach einem Hoch im August flacht sie leicht ab.</p>
  <svg class="abs" style="left:16px;top:100px" width="340" height="150" viewBox="0 0 340 150" aria-label="Liniendiagramm Reichweite und Interaktionen">
    <g font-family="Inter, Arial, sans-serif" font-size="10" fill="#4d5f64">
      <text x="0" y="14">05</text><text x="0" y="42">45</text><text x="0" y="70">23</text><text x="0" y="98">62</text><text x="0" y="126">10</text>
    </g>
    <g stroke="#e2e7e8" stroke-width="1">
      <line x1="24" y1="10" x2="336" y2="10"/><line x1="24" y1="38" x2="336" y2="38"/>
      <line x1="24" y1="66" x2="336" y2="66"/><line x1="24" y1="94" x2="336" y2="94"/>
      <line x1="24" y1="122" x2="336" y2="122"/>
    </g>
    <path d="M115 130 C130 95,145 50,170 45 C190 42,200 70,210 85 C220 100,235 105,250 95" fill="none" stroke="#809398" stroke-width="1.5"/>
    <path d="M98 110 C120 85,145 55,170 35 C190 18,210 12,225 25 C235 40,238 80,242 100" fill="none" stroke="#11323a" stroke-width="2"/>
    <path d="M140 58 l4 -6 l4 6 z" fill="#f69f25"/>
    <circle cx="95" cy="123" r="14" fill="#fbd39b"/>
    <circle cx="228" cy="24" r="13" fill="#809398"/>
    <circle cx="258" cy="123" r="14" fill="#f69f25"/>
  </svg>
</section>

<section class="panel bars">
  <div class="panel-head" style="left:16px">Social Share 2023</div>
  <div class="panel-head" style="left:171px">Social Share 2023</div>
  <h2 class="abs chart-title">Beitrag Reichweite Monat</h2>
  <svg class="abs" style="left:0;top:0" width="374" height="262" viewBox="0 0 374 262" aria-label="Balkendiagramm Beiträge pro Monat">
    <g stroke="#e2e7e8"><line x1="50" y1="94" x2="345" y2="94"/><line x1="50" y1="118" x2="345" y2="118"/><line x1="50" y1="142" x2="345" y2="142"/><line x1="50" y1="166" x2="345" y2="166"/><line x1="50" y1="190" x2="345" y2="190"/></g>
    <g font-family="Inter, Arial, sans-serif" font-size="13" fill="#4d5f64"><text x="31" y="98">#</text><text x="31" y="122">#</text><text x="31" y="146">#</text><text x="31" y="170">#</text><text x="31" y="194">#</text></g>
    <rect x="95" y="179" width="19" height="26" rx="5" fill="#11323a"/>
    <rect x="153" y="126" width="19" height="79" rx="5" fill="#d3dcdd"/>
    <rect x="183" y="185" width="19" height="20" rx="5" fill="#fbd39b"/>
    <rect x="213" y="146" width="19" height="59" rx="5" fill="#809398"/>
    <rect x="243" y="112" width="19" height="93" rx="5" fill="#f69f25"/>
    <rect x="273" y="179" width="19" height="26" rx="5" fill="#d3dcdd"/>
    <rect x="303" y="179" width="19" height="26" rx="5" fill="#f69f25"/>
    <g font-family="Inter, Arial, sans-serif" font-size="10" fill="#4d5f64" text-anchor="middle">
      <text x="104" y="222">12</text><text x="133" y="222">12</text><text x="162" y="222">42</text><text x="192" y="222">52</text><text x="222" y="222">12</text><text x="252" y="222">22</text><text x="282" y="222">12</text><text x="312" y="222">29</text>
    </g>
  </svg>
</section>

<section class="panel cards">
  <div class="panel-head" style="left:16px">Audience 2024</div>
  <div class="panel-head" style="left:170px">Social Share 2022</div>
  <article class="card card-orange">
    <h3>Social Media<br>Performance Report</h3>
    <p>Die wichtigsten Kennzahlen des Quartals auf einen Blick für Ihr Team.</p>
    <p>Reichweite, Klicks und neue Follower haben sich positiv entwickelt. Beiträge mit klarer Botschaft und starkem Bild erzielten die besten Werte im gesamten Zeitraum.</p>
  </article>
  <article class="card card-slate">
    <h3>Social Media<br>Profil Report</h3>
    <p>Profilbild, Titel und Beschreibung wurden geprüft und bewertet. Die Angaben sind vollständig, jedoch fehlen klare Schlagworte für die Suche. Wir empfehlen eine kürzere Info, einen Link zur Website und eine einheitliche Bildsprache für alle Beiträge im nächsten Quartal.</p>
  </article>
  <div class="chips" style="left:18px"><span class="chip"><i style="background:var(--brand-teal)"></i>Profil</span><span class="chip"><i style="background:var(--brand-orange)"></i>Inhalte</span></div>
  <div class="chips" style="left:108px"><span class="chip"><i style="background:var(--brand-teal)"></i>Fans</span><span class="chip"><i style="background:var(--brand-slate)"></i>Reichweite</span></div>
</section>

<section class="panel feature feature-a">
  <div class="panel-head" style="left:16px">Social Media 2024</div>
  <div class="panel-head" style="left:190px">Social Check</div>
  <h2 class="abs feature-title">Marketing Post Ready<br>Monthly Report</h2>
  <p class="abs body-text" style="left:16px;top:95px;width:165px">Diese Beiträge haben im Monat die meisten Reaktionen erhalten. Wir zeigen, welche Formate gut ankommen und wie sich Kommentare verteilen.</p>
  <p class="abs body-text" style="left:16px;top:148px;width:165px">Bei der Planung empfehlen wir einen festen Rhythmus und kurze Texte mit klarer Frage am Ende, um den Dialog zu fördern.</p>
  <p class="abs body-text" style="left:16px;top:197px;width:330px">Die besten Beiträge erhielten im Schnitt 24 Prozent mehr Reaktionen als im Vorquartal.</p>
  <div class="photo" style="left:196px;top:40px;width:163px;height:148px;background:linear-gradient(160deg,#f1d9d3,#d9a99c)" role="img" aria-label="Foto: Hände halten ein Smartphone mit App-Übersicht"></div>
  <div class="action-bar">Zum Report</div>
</section>

<section class="panel feature feature-b">
  <div class="panel-head" style="left:16px">Social Trend</div>
  <div class="panel-head" style="left:175px">Social Trend</div>
  <h2 class="abs feature-title">Wachstum Medien<br>Performance Trend</h2>
  <p class="abs feature-sub">Wachstum Q3</p>
  <p class="abs body-text" style="left:16px;top:108px;width:160px">Videos und kurze Beiträge legten im Quartal am stärksten zu. Auch Umfragen und Bildserien zeigen steigende Werte. Für das nächste Quartal raten wir zu mehr Bewegtbild, einer klaren Redaktion und einem festen Zeitplan für alle Kanäle, damit Ihr Profil weiter sichtbar bleibt.</p>
  <div class="photo" style="left:195px;top:40px;width:162px;height:148px;background:linear-gradient(160deg,#eeeeec,#3c3a3b)" role="img" aria-label="Foto: Frau mit Brille schaut nachdenklich zur Seite"></div>
  <div class="action-bar">Mehr erfahren</div>
</section>

</body>
</html>
```